Four Quiet Steps Toward a Stronger Offer on THE Property - VARN Real Estate

I have written an E-Book that is called "Four Quiet Steps Toward a Stronger Offer on The Property." The E-Book will be available as a FREE download from my VARN Real Estate landing page, and also from a Chatterbox campaign that will be commencing in early September.

The E-Book content is in the WORD document below - I now need for it to be made to look more professional and suitable for publishing and placed on my landing page for download. Please review and send me some proposals for this e-book to be a bit more eye catching and appealing than just a WORD doc.

My VARN Real Estate landing page is still under development and you can see the what is close to the final proposal here:

http://www.plum-orbit.com.au/varn/

The cover of the E-Book is at the bottom of the page. Please review and give the internals the sale look and feel.

Target Market(s)

Home and Property Owners in the middle ring Eastern Suburbs of Melbourne - approximately 15 - 30 km's from the central business district. The area is a very family oriented area and features mostly houses that are 3 or 4 bedroom - with some larger properties that are five or more bedrooms. The area is quite an expensive suburban community and house prices range between the low of $1,000,000 to a high of more than $2,500,000. The predominant cultural group that buys in this area are Chinese and Chinese Australian buyers. The predominant group who are selling are usually Australians of a white anglo-saxon background. Other groups are of Asian sub continent background (Indian / Sri Lankan/ Pakistan). All are families that are attracted to the area because of the great schools, good shopping, leisure facilities (parks, pools, courts etc), and excellent public and road transport infrastructure. Read the content of my e-book - it tells you every thing you need to know :)

Industry/Entity Type

Real Estate

Colors

Designer to choose colors to be used in the design.

Requirements
Must have
• Once completed the layout should not be too busy - it should be easy to read. I guess then the statement "less is more" is applicable.
• I will probably print a number of copies of this book for distribution as well - so please consider print attributes in the design.
• IMPORTANT: as for any e-book offering specialist advice, the MAIN reason for the book is for the generation of sales leads and to establish the author as a subject matter expert on the topic. Please consider this in your design elements. BUT - the book should also not come across as 1 big advertisement either. Subtle but impactful are well chosen words to describe how it should present.
Nice to have
• VARN Real Estate branding on every page - to re-inforce the message.
Should not have
• No need for animations or illustrations/

```html
<!DOCTYPE html>
<html lang="en">
<head>
<meta charset="utf-8">
<title>VARN Real Estate – E-Book Spreads</title>
<link href="https://fonts.googleapis.com/css2?family=Montserrat:wght@500;600;700&family=Roboto+Condensed:wght@400;700&display=swap" rel="stylesheet">
<style>
:root{
  --backdrop:#1d1d1d;
  --paper:#ffffff;
  --mint:#5cc4a2;
  --ink:#2b2b2b;
  --body:#3a3a3a;
  --rule:#c9c9c9;
  --band:#2a2a2a;
  --link:#2b3fb5;
}
*{margin:0;padding:0;box-sizing:border-box}
html,body{width:1077px;height:1200px;overflow:hidden;background:var(--backdrop)}
.stage{position:absolute;left:0;top:0;width:1300px;height:1449px;transform:scale(0.8285);transform-origin:0 0}
.spread{position:absolute;left:270px;width:760px;height:538px;display:flex}
.spread--one{top:98px}
.spread--two{top:813px}
.page{position:relative;width:380px;height:538px;background:var(--paper);overflow:hidden;font-family:"Roboto Condensed",sans-serif;color:var(--body)}
.page--left{box-shadow:inset -8px 0 10px -8px rgba(0,0,0,.18)}
.page--right{box-shadow:inset 8px 0 10px -8px rgba(0,0,0,.18)}
.body-text{font-size:5.7px;line-height:10px;text-align:justify}
.body-text p+p{margin-top:10px}
.footer-rule{position:absolute;left:0;right:16px;top:516px;height:1px;background:var(--rule)}
.footer-tab{position:absolute;left:0;top:514px;width:27px;height:3px;background:var(--mint)}
.page--right .footer-rule{left:0}
.page-num{position:absolute;left:14px;top:520px;font-family:Montserrat,sans-serif;font-weight:600;font-size:11px;color:var(--mint)}
.page--right .page-num{left:10px}
.brand{position:absolute;right:10px;top:512px;font-family:Montserrat,sans-serif;font-weight:700;font-size:14px;letter-spacing:1px;color:var(--ink)}
.phone{position:absolute;right:16px;top:519px;font-size:8px;color:var(--body);display:flex;align-items:center;gap:2px}
.section-head{position:absolute;font-family:Montserrat,sans-serif;font-weight:600;color:var(--mint);font-size:14px;line-height:15px;padding-left:11px}
.section-head::before{content:"";position:absolute;left:0;top:3px;width:8px;height:8px;background:var(--ink)}
.section-head--light{color:#fff}
.section-head--light::before{background:#fff}
.photo{position:absolute}
/* page 03 */
.chapter-block{position:absolute;left:27px;top:29px;width:325px;height:156px;background:var(--mint)}
.chapter-icon{position:absolute;left:10px;top:88px;width:55px;height:58px;background:rgba(255,255,255,.35)}
.chapter-title{position:absolute;left:77px;top:90px;font-family:Montserrat,sans-serif;font-weight:600;color:#fff;font-size:17px;line-height:19px}
.col{position:absolute}
/* page 04 */
.kicker{position:absolute;left:35px;top:33px;font-size:7px;color:var(--ink)}
.tips-title{font-weight:700;color:var(--ink);margin-left:8px}
.tips{list-style:none;margin-left:8px}
.tips li{position:relative;padding-left:6px}
.tips li::before{content:"";position:absolute;left:0;top:4px;width:2.5px;height:2.5px;border-radius:50%;background:var(--mint)}
.link{color:var(--link);text-decoration:underline}
.band{position:absolute;left:0;top:294px;width:380px;height:198px;background:var(--band)}
.band .body-text{color:#f1f1f1}
</style>
</head>
<body>
<div class="stage">

  <section class="spread spread--one">
    <article class="page page--left">
      <div class="chapter-block">
        <div class="chapter-icon" role="img" aria-label="Line icon of a presenter beside an easel showing a house"></div>
        <h1 class="chapter-title">01<br>PROPERTY<br>PRESENTATION:</h1>
      </div>
      <div class="col body-text" style="left:35px;top:200px;width:140px">
        <p>Like any product – the newer, the cleaner, the shinier, and the better presented a property is for sale…then the more interest it will attract from prospective Buyers.<br>The more Buyer interest that a property attracts…the more competition around the purchase price that will be created.<br>And Buyer competition is fantastic if you know how to harness it to achieve the best possible sale price. But where is it that you should begin and how?<br>So let's start at the very beginning – property preparation and presentation for sale.<br>It is important to state that very few people actually live in the manner that a house is presented for sale. In most instances what you see at homes that are open for Buyer inspection is the end result of a lot of hard work on behalf of the Vendor and others.<br>So don't be concerned – however and whatever your home looks like now…it can be transformed to maximize its appeal to Buyers.</p>
      </div>
      <div class="col body-text" style="left:205px;top:200px;width:140px">
        <p>"Vendors will always see all of the great and wonderful aspects of their property in an effort to create value and push up the price; a Buyer will always tell you everything that is wrong in an effort to drive down the price."<br>The whole process of buying and selling property is very psychological and highly emotional for most people, so it is very important for Vendors to place themselves in the shoes of a Buyer when running a critical eye across the presentation preparations.<br>Your property should be polished, displayed and presented to the highest possible standard. That standard will be different for everyone – factoring in age, ability, financial capacity, the size of family, number of pets and so on.<br>In addition - every property is different, and every property has its own features and personality – what's important is to amplify the positives and minimize the impact of the negatives throughout the home.</p>
      </div>
      <div class="photo" role="img" aria-label="Dusk photo of a lit modern home with a sold sign" style="left:35px;top:416px;width:102px;height:78px;background:linear-gradient(180deg,#1d3f78 0%,#3a5a8c 45%,#3c4a2a 100%)"></div>
      <div class="photo" role="img" aria-label="Photo of a modern two-storey home with a sold sign" style="left:139px;top:416px;width:101px;height:78px;background:linear-gradient(180deg,#6d8fb2 0%,#7d7e7c 55%,#4c5a3a 100%)"></div>
      <div class="photo" role="img" aria-label="Twilight photo of a brick home with a sold sign" style="left:243px;top:416px;width:101px;height:78px;background:linear-gradient(180deg,#2f5fa8 0%,#9a6a44 60%,#5a3a22 100%)"></div>
      <div class="footer-tab"></div><div class="footer-rule"></div>
      <span class="page-num">03</span>
      <span class="brand">VARN</span>
    </article>

    <article class="page page--right">
      <p class="kicker">LET'S LOOK AT SOME OF THE BASICS:</p>
      <h2 class="section-head" style="left:25px;top:52px">CURBSIDE APPEAL</h2>
      <div class="col body-text" style="left:35px;top:67px;width:310px">
        <p>First impressions count - stand outside at the front of your house on the street and look at your house with a critical eye. Does your home stand out as a welcoming and "happy" place to arrive at?</p>
        <p>Tidy the gardens, mow the lawns, repair the gutters, paint under the eaves of the roof, clean the windows, repair the cracks in the cement driveways and do some basic landscaping such as adding mulch to garden beds (my personal preference for mulch is black tan bark – but other varieties are just as effective). You will find all these tasks make a huge difference to the exterior look and feel of your property.</p>
        <p>If your property has a fence, then clean it and paint it. Cut back any overgrown trees and bushes, trim and shape the edges of pathways, and clear and remove all rubbish (including rubbish bins) from the front of the house.<br>By improving your properties curbside appeal and street presence you will not only allow Buyers to have an immediate positive first impression – you are also ensuring that the property is ready to be photographed for the all important exterior façade shot as part of the marketing and advertising.</p>
      </div>
      <h2 class="section-head" style="left:25px;top:218px">CLEANING AND DE-CLUTTERING</h2>
      <div class="col body-text" style="left:35px;top:233px;width:310px">
        <p>If you have been living in your home for anymore than a few years, then you might be surprised at the amount of "things" that you have accumulated. Most people do not genuinely live in the manner that they present a property when they sell. And less is definitely more when it comes to the sale of your home and the reduction of "things" in the home.<br>Our friends at <span class="link">www.tidyhouseplan.com.au offer the following tips when it comes to de-cluttering:</span></p>
        <p class="tips-title" style="margin-top:6px">Top Tips on How to De-clutter your Home</p>
        <ul class="tips">
          <li>Just start. Don't overthink it; just start getting rid of things!</li>
          <li>Deal with rubbish first. Start by going through each room with a big garbage bag and throwing away anything that isn't saleable or suitable for charity.</li>
          <li>De-clutter by category not by room. It is less overwhelming to de-clutter by category (such as clearing out DVD's or linen) than to tackle a whole room.</li>
          <li>It's about progress not perfection. Don't be discouraged, clutter takes time to build up and it will take time to deal with.</li>
          <li>If you don't need it, why not donate it or throw it away?</li>
          <li>Remove all books from bookcases.</li>
          <li>Pack up those knickknacks.</li>
          <li>Clean off everything on kitchen counters.</li>
          <li>Put essential items used daily in a small box that can be stored in a closet when not in use.</li>
          <li>Think of this process as a head start on the packing you will eventually need to do anyway.</li>
        </ul>
        <p style="margin-top:4px">Of equal importance is the organization and arrangement of the areas that cannot be immediately seen. Cupboards, closets, linen presses and pantries inside the property. Buyers WILL open and look inside pantries, cupboards and wardrobes – so the more organized they are the better impression a Buyer will have of the property.</p>
        <p>If you have a lot of packing boxes and surplus furniture to be removed and put away, and an off-site storage space is not an option…then a garage on the property can be used so long as items are neatly packed and safely stored.</p>
      </div>
      <div class="footer-tab"></div><div class="footer-rule"></div>
      <span class="page-num">04</span>
      <span class="phone"><svg width="7" height="7" viewBox="0 0 10 10" aria-hidden="true"><path d="M2 1l2 2-1 1.5c.6 1.2 1.4 2 2.5 2.5L7 6l2 2-1.5 1.5C4.5 9 1 5.5.5 2.5z" fill="none" stroke="#555" stroke-width="0.9"/></svg>1800 555 019</span>
    </article>
  </section>

  <section class="spread spread--two">
    <article class="page page--left">
      <h2 class="section-head" style="left:27px;top:44px">MAINTENANCE<br>&amp; PAINTING</h2>
      <div class="col body-text" style="left:35px;top:82px;width:150px">
        <p>Walk through your property and check that all lights are working (replace the globes if they are not working); identify and fill any cracks in the walls, floor and ceiling; apply a coat or two of paint externally and internally.</p>
        <p>Paint can hide a lot of sins – and also provides a new lease on life for homes that have been well lived in. Weatherboard / timber homes in particular freshen up very well externally following a coat of paint. Professional painters can be expensive if they are required to complete the entire house internally and externally. However…the cost is quite likely recovered through the increased price achieved on the sale of your home.</p>
        <p>No matter what anyone – including agents – will tell you…NO BUYER is interested in looking at peeling paint, and they may even start questioning as to what else is wrong in the property and start talking the price down. We don't want that to happen to your property.</p>
      </div>
      <div class="photo" role="img" aria-label="Photo of a freshly painted two-storey house at dusk" style="left:198px;top:40px;width:146px;height:110px;background:linear-gradient(180deg,#2f6fc4 0%,#7fa3c8 50%,#5a6b4a 100%)"></div>
      <div class="photo" role="img" aria-label="Photo of a grey weatherboard family home with a green lawn" style="left:198px;top:154px;width:146px;height:123px;background:linear-gradient(180deg,#8cc0e0 0%,#8e9398 50%,#5c8a3c 100%)"></div>
      <div class="band">
        <h2 class="section-head section-head--light" style="left:27px;top:26px">PROFESSIONAL HOME STAGING/ STYLING</h2>
        <div class="col body-text" style="left:37px;top:50px;width:145px">
          <p>One of the BEST investments you can make in the sale of your home is having your home professionally "staged" by a stylist.</p>
          <p>Stylists are property presentation experts who concentrate on displaying your property in the best possible manner for sale.</p>
          <p>A stylist can add tens of thousands of dollars to the price of a property – simply by adding their design creativity.</p>
        </div>
        <div class="col body-text" style="left:203px;top:50px;width:145px">
          <p>For properties that have no furniture – "staging" is very important in order to engage Buyers emotionally in the home.</p>
          <p>Furniture, window dressings, wall hangings and decorations create the "soul" of any home. I have experienced many a Buyer across the years be disappointed at the final inspection prior to settlement, when they realize what they have purchased is just four walls, a ceiling and an empty room, as it was all so beautifully styled and presented as a dream lifestyle at the time of sale.</p>
        </div>
      </div>
      <div class="footer-tab"></div><div class="footer-rule"></div>
      <span class="page-num">05</span>
      <span class="brand">VARN</span>
    </article>

    <article class="page page--right">
      <h2 class="section-head" style="left:25px;top:44px">RENOVATION VERSUS<br>COSMETIC IMPROVEMENT</h2>
      <div class="col body-text" style="left:35px;top:82px;width:143px">
        <p>Renovate and make money! This claim is made constantly but is it true? Would you be better off merely doing some basic cosmetic work to improve presentation rather than renovating?</p>
        <p>Renovating with the purpose of the homeowner staying in the property with an improved lifestyle is quite different to renovating for the purpose of making a profit. It's important to be aware that renovation is no guarantee to making a profit.</p>
        <p>Would-be renovators need to be aware that with respect to the value of a property there are two counter-forces at work.</p>
        <p>Firstly, there is the land on which the building sits. The price of land appreciates according to market demand and the popularity of the locality. On the other hand most buildings depreciate in value, eventually to the point that their very presence actually devalues a site. In other words the site would be worth more without the building than with it.</p>
        <p>Whilst renovating a building undoubtedly improves the value of a property, there's the question as to whether the consequential improvement in value will be sufficient for the investment in the renovation to be profitable.</p>
        <p>Though many people would claim that they have renovated and profited, the question arises would</p>
      </div>
      <div class="col body-text" style="left:202px;top:82px;width:143px">
        <p>they have profited by a greater amount simply by tidying up and perhaps repainting, thus saving the cost of renovation?</p>
        <p>It's a different matter if you're able to renovate to a professional standard yourself: you're saving the substantial cost of labour. But if you have to hire people – then think about it carefully!</p>
        <p>There is some suggestion that the smaller the land area is, in proportion to the overall property value, so the better the proposition of renovation. In other words a renovation project may be a better proposition for giving a return in an old townhouse or home unit rather than a home on a full block.</p>
        <p>One well-known cautionary measure is to weigh the cost of any improvements you want to make against the overall values in your neighbourhood. If you over-improve for the neighbourhood, you may not boost your property value sufficiently to recover the costs, let alone turn the cost into additional profit.</p>
        <p>So in summary - a well-presented property is very important in capturing Buyer interest and selling your home for the best price. How far you go to create the impression of a perfect lifestyle property is your decision, and your Agent can provide advice as to what "polishing" should be done at a minimum to help you achieve the best price.</p>
      </div>
      <div class="photo" role="img" aria-label="Black and white photo of a modern white kitchen" style="left:36px;top:401px;width:308px;height:92px;background:linear-gradient(180deg,#6a6a6a 0%,#b9b9b9 40%,#e6e6e6 100%)"></div>
      <div class="footer-tab"></div><div class="footer-rule"></div>
      <span class="page-num">06</span>
      <span class="phone"><svg width="7" height="7" viewBox="0 0 10 10" aria-hidden="true"><path d="M2 1l2 2-1 1.5c.6 1.2 1.4 2 2.5 2.5L7 6l2 2-1.5 1.5C4.5 9 1 5.5.5 2.5z" fill="none" stroke="#555" stroke-width="0.9"/></svg>1800 555 019</span>
    </article>
  </section>

</div>
</body>
</html>
```